Redesign (8 documents) attached with brand guidelines - very quick/easy job!

We have 8 flyers/documents that we need put into the style of our new brand (see attached). So this is a simple rebrand exercise - complete with our brand guidelines (see attached)

I would need the designer to sign an NDA prior to taking this piece of work as I will be sharing newly branded documents with you prior to market release.

If these are done well we would as the same designer to work on a z-card designed brochure/POS

Brief:

- These are documents that customers would need to complete in order to book a particular service
- If you use images (ideally from Pixmora, so we don’t have to pay for them!)
- Icon ideas enclosed
-All the content on the brochures is required: but if you think it would 'flow better' in a different order that is fine.

Customers interested in receiving a particular service

Work

• Brandon (see brand guide)

• A4
• New logo ideas
• Anything out of brand guidleines

```html
<!DOCTYPE html>
<html lang="en">
<head>
<meta charset="utf-8">
<title>Health Objectives Form</title>
<link rel="stylesheet" href="https://fonts.googleapis.com/css2?family=Outfit:wght@400;500;600;700&display=swap">
<style>
  :root {
    --teal: #00a9c6;
    --yellow: #f5ec00;
    --lime: #b3d334;
    --orange: #f7941d;
    --pink: #e5439a;
    --grey: #9b9b9b;
    --ink: #555a5e;
    --rule: #c9c9c9;
    --paper: #ffffff;
    --backdrop: #e6e6e6;
  }
  * { box-sizing: border-box; margin: 0; padding: 0; }
  html, body {
    width: 1200px; height: 1000px; overflow: hidden;
    background: var(--backdrop);
    font-family: "Outfit", "Helvetica Neue", Arial, sans-serif;
    color: var(--ink);
  }
  .sheet {
    position: absolute; left: 260px; top: 20px;
    width: 680px; height: 960px;
    background: var(--paper);
  }
  .brand-tab {
    position: absolute; left: 0; top: 44px;
    width: 234px; height: 80px;
    background: var(--teal);
    border-radius: 0 40px 40px 0;
    display: flex; align-items: center; padding-left: 44px;
  }
  .brand-name {
    color: var(--yellow); font-weight: 600; font-size: 27px; letter-spacing: 0.5px;
  }
  .form-title {
    position: absolute; left: 33px; top: 139px;
    width: 613px; height: 31px;
    background: var(--teal); color: #fff;
    font-weight: 600; font-size: 19px;
    display: flex; align-items: center; justify-content: center;
  }
  .field {
    position: absolute; font-size: 13.5px; white-space: nowrap;
    display: flex; align-items: baseline;
  }
  .field .dots {
    display: inline-block; border-bottom: 1.5px dotted var(--ink);
    margin-left: 4px; height: 10px;
  }
  .objectives {
    position: absolute; left: 33px; top: 246px;
    width: 613px; height: 679px;
    background: var(--teal);
    border-radius: 14px;
    padding: 6px 6px;
    display: flex; flex-direction: column; gap: 8px;
  }
  .reason {
    background: var(--paper);
    display: flex; flex-direction: column; height: 329px;
  }
  .reason:first-child { border-radius: 8px 8px 0 0; overflow: hidden; }
  .reason:last-child { border-radius: 0 0 8px 8px; overflow: hidden; }
  .reason-head {
    height: 25px; flex: none; background: var(--yellow);
    display: flex; font-weight: 500; color: #0b7f95; font-size: 13.5px;
  }
  .reason-head span { display: flex; align-items: center; padding-left: 16px; }
  .col-label { width: 216px; flex: none; border-right: 1px solid var(--rule); }
  .col-answer { flex: 1; }
  .row {
    height: 73px; flex: none; display: flex; border-top: 1px solid var(--rule);
  }
  .row:last-child { flex: 1; height: auto; }
  .reason-head + .row { border-top: none; }
  .row .col-label {
    font-size: 10.5px; line-height: 1.28; padding: 11px 12px 0 16px;
  }
  .row:last-child .col-label { padding-top: 9px; }
  .colour-strip {
    position: absolute; left: 0; bottom: 0; width: 680px; height: 16px; display: flex;
  }
  .colour-strip span { flex: 1; }
</style>
</head>
<body>
  <main class="sheet">
    <div class="brand-tab"><span class="brand-name">VITALANE</span></div>

    <h1 class="form-title">Health Objectives</h1>

    <div class="field" style="left:33px;top:186px;">Nutritionist’s name :<span class="dots" style="width:142px"></span></div>
    <div class="field" style="left:358px;top:186px;">Client’s name :<span class="dots" style="width:193px"></span></div>
    <div class="field" style="left:33px;top:215px;">Store location :<span class="dots" style="width:178px"></span></div>
    <div class="field" style="left:358px;top:215px;">Date of consultation :<span class="dots" style="width:147px"></span></div>

    <section class="objectives">
      <div class="reason">
        <div class="reason-head"><span class="col-label">Reason 1</span><span class="col-answer">Your comments</span></div>
        <div class="row"><div class="col-label">Symptom, issue or condition you want to address.</div><div class="col-answer"></div></div>
        <div class="row"><div class="col-label">Duration - how long have you felt like this or experienced this symptom(s)?</div><div class="col-answer"></div></div>
        <div class="row"><div class="col-label">Have you seen a doctor about this for a diagnosis? Did you receive any medical treatment?</div><div class="col-answer"></div></div>
        <div class="row"><div class="col-label">Is there any background or extra health or lifestyle information that relates to this situation that you want your practitioner to know about? Please give details.</div><div class="col-answer"></div></div>
      </div>
      <div class="reason">
        <div class="reason-head"><span class="col-label">Reason 2</span><span class="col-answer">Your comments</span></div>
        <div class="row"><div class="col-label">Symptom, issue or condition you want to address.</div><div class="col-answer"></div></div>
        <div class="row"><div class="col-label">Duration - how long have you felt like this or experienced this symptom(s)?</div><div class="col-answer"></div></div>
        <div class="row"><div class="col-label">Have you seen a doctor about this for a diagnosis? Did you receive any medical treatment?</div><div class="col-answer"></div></div>
        <div class="row"><div class="col-label">Is there any background or extra health or lifestyle information that relates to this situation that you want to practitioner to know about? Please give details.</div><div class="col-answer"></div></div>
      </div>
    </section>

    <div class="colour-strip">
      <span style="background:var(--teal)"></span>
      <span style="background:var(--yellow)"></span>
      <span style="background:var(--lime)"></span>
      <span style="background:var(--orange)"></span>
      <span style="background:var(--pink)"></span>
      <span style="background:var(--grey)"></span>
    </div>
  </main>
</body>
</html>
```